Powerpoint master slides for business

Hello everyone,

I am looking for a new PowerPoint master slide that should be modern, slim and yet suitable for business.

I have uploaded a few pictures, which should serve as A. orientation for my presentation. A logo should be placed on the right-hand side of the cover sheet and all subsequent slides - please insert a placeholder here. Also attached are our company colors, which must be taken into account.

Basically, I would find 6 to 10 slides (cover sheet, classic slide, end, etc.) good.

PS: The slides are intended for general everyday work, ie the design should be subtle and easily adaptable to different situations, but still look chic, modern and classy.

```html
<!DOCTYPE html>
<html lang="en">
<head>
<meta charset="utf-8">
<title>Business Master Slides</title>
<link href="https://fonts.googleapis.com/css2?family=Montserrat:ital,wght@0,400;0,500;0,600;0,700;1,600;1,700&family=Roboto:wght@400;500&display=swap" rel="stylesheet">
<style>
:root{
  --bg:#d6d7d9;
  --paper:#ffffff;
  --ink:#222222;
  --dark:#2b2b2b;
  --mid:#6f6f6f;
  --grey:#a6a6a6;
  --light:#d9d9d9;
  --faint:#ececec;
  --muted:#9a9a9a;
}
*{box-sizing:border-box;margin:0;padding:0}
html,body{width:1038px;height:1200px;overflow:hidden;background:var(--bg)}
body{font-family:'Montserrat',sans-serif;color:var(--ink)}
.canvas{position:relative;width:1038px;height:1200px;background:var(--bg);overflow:hidden}
.slide{position:absolute;width:257px;height:145px;background:var(--paper);overflow:hidden;box-shadow:0 1px 3px rgba(0,0,0,.12)}
.abs{position:absolute}
.tiny{font-size:3px;line-height:4px;color:var(--muted)}
.tiny.light{color:#bbb}
.center{text-align:center}
.justify{text-align:justify}
.photo{position:absolute;background:linear-gradient(135deg,#cfcfcf,#8a8a8a)}
.tag{position:absolute;left:0;display:flex;align-items:center;gap:4px;font-size:6.5px;font-weight:500;letter-spacing:.1px;color:var(--ink);white-space:nowrap}
.tag::before{content:"";width:11px;height:5px;background:var(--dark)}
.tag b{font-weight:600}
.social{position:absolute;display:flex;gap:2px}
.social span{width:6.5px;height:6.5px;border-radius:50%;background:var(--dark)}
.italic-title{font-style:italic;font-weight:700;color:var(--ink)}
.portrait{position:absolute;border-radius:50%;border:2px solid var(--paper);background:radial-gradient(circle at 50% 40%,#e9e4df,#a9a39d)}
.member-name{position:absolute;font-size:4.6px;font-weight:700;color:var(--paper);text-align:center;width:60px}
.member-note{position:absolute;width:56px;font-size:2.4px;line-height:3.2px;color:#bbb;text-align:center}
svg text{font-family:'Montserrat',sans-serif}
</style>
</head>
<body>
<div class="canvas">

  <section class="slide cover" style="left:111px;top:141px;background:var(--dark)">
    <div class="photo" role="img" aria-label="Dark monochrome photo of office towers" style="inset:0;background:linear-gradient(160deg,#3a3a3a,#232323 60%,#2f2f2f)"></div>
    <div class="abs center" style="left:0;right:0;top:50px;color:#fff">
      <div style="font-size:9.5px;font-weight:500">Welcome to Our</div>
      <div style="font-size:12.5px;font-weight:600;margin-top:1px">Presentation Name</div>
      <div style="font-size:9.5px;font-weight:500">Description</div>
    </div>
  </section>

  <section class="slide intro" style="left:390px;top:136px;background:var(--dark)">
    <div class="photo" role="img" aria-label="Dark desk scene with laptop, phone, pen and notebook" style="inset:0;background:linear-gradient(120deg,#4a4a4a,#2a2a2a 45%,#1f1f1f)"></div>
    <div class="abs" style="left:145px;top:71px;width:100px;color:#fff;text-align:center">
      <div style="font-size:5.3px;letter-spacing:.8px">YOUR SUBTITLE TEXT HERE</div>
      <div style="font-size:8.6px;font-weight:700;letter-spacing:.6px;margin-top:1px">COMPANY NAME</div>
    </div>
    <p class="abs tiny justify" style="left:108px;top:109px;width:134px;color:#777">Our team delivers clear strategy and steady results for every client. We plan with care, work with focus and report with honesty. This short note sets the tone for the story that follows in the next slides of the deck.</p>
  </section>

  <section class="slide about" style="left:670px;top:136px">
    <div class="abs" style="left:24px;top:24px">
      <div class="italic-title" style="font-size:14px;line-height:14px">About</div>
      <div style="font-size:8.5px;font-style:italic;font-weight:600;line-height:10px">Title<br>Presentation</div>
    </div>
    <p class="abs tiny justify" style="left:24px;top:69px;width:62px">A short summary of the company, its people and its goals. Replace this text with your own message to suit the topic of the slide.</p>
    <div class="social" style="left:24px;top:113px"><span></span><span></span><span></span></div>
    <div class="photo" role="img" aria-label="Silhouettes of people at a window overlooking a city" style="left:119px;top:20px;width:119px;height:42px;background:linear-gradient(180deg,#9a9a9a,#3a3a3a)"></div>
    <div class="abs" style="left:118px;top:69px;width:50px;height:55px;background:var(--dark);color:#fff">
      <div style="font-size:5.5px;font-style:italic;font-weight:600;text-align:center;margin-top:6px">About</div>
      <div style="width:6px;height:.6px;background:#fff;margin:2px auto 3px"></div>
      <p class="tiny justify" style="font-size:2.3px;line-height:3px;color:#ccc;padding:0 6px">A short summary of the company, its people and its goals. Replace this text with your own message to suit the topic of the slide.</p>
    </div>
    <div class="photo" role="img" aria-label="Black and white photo of a man in a tuxedo" style="left:171px;top:67px;width:66px;height:55px;background:linear-gradient(180deg,#d8d8d8,#3b3b3b)"></div>
  </section>

  <section class="slide company" style="left:111px;top:293px">
    <div class="photo" role="img" aria-label="Light grey triangle pattern" style="left:0;top:0;width:73px;height:145px;background:linear-gradient(100deg,#e6e8ea,#f6f7f8 70%,#fff)"></div>
    <div class="abs center" style="left:40px;right:40px;top:57px">
      <div style="font-size:3.2px;color:var(--muted);letter-spacing:.2px">YOUR BUSINESS SOLUTIONS</div>
      <div style="font-size:7.8px;font-weight:600;color:#444;letter-spacing:.2px">COMPANY NAME</div>
      <p class="tiny light" style="margin-top:4px">A short summary of the company, its people and its goals. Replace this text with your own message to suit the topic of the slide.</p>
    </div>
    <div class="abs center" style="left:113px;top:107px;width:31px;height:7px;border-radius:4px;background:var(--mid);color:#fff;font-size:3.3px;line-height:7px">Learn More</div>
  </section>

  <section class="slide about-us" style="left:390px;top:293px">
    <div class="abs center" style="left:0;right:0;top:20px;font-size:7.8px;color:#444">About Us</div>
    <p class="abs tiny center" style="left:60px;right:60px;top:32px">Short role note for this team member goes right here.</p>
    <div class="photo" role="img" aria-label="Business team smiling in a meeting" style="left:45px;top:52px;width:166px;height:46px;background:linear-gradient(90deg,#c9b9a8,#e4e0dc 40%,#7d8797 70%,#d6d0c8)"></div>
    <p class="abs tiny center" style="left:22px;right:22px;top:108px">Our team delivers clear strategy and steady results for every client. We plan with care, work with focus and report with honesty. This short note sets the tone for the story that follows in the next slides of the deck.</p>
  </section>

  <section class="slide teams" style="left:670px;top:293px">
    <div class="tag" style="top:9px"><span>OUR TEAMS</span></div>
    <div class="abs" style="left:0;right:0;top:66px;bottom:0;background:var(--dark)"></div>
    <div class="portrait" role="img" aria-label="Portrait of team member" style="left:33px;top:42px;width:50px;height:50px"></div>
    <div class="portrait" role="img" aria-label="Portrait of team member" style="left:103px;top:42px;width:50px;height:50px"></div>
    <div class="portrait" role="img" aria-label="Portrait of team member" style="left:174px;top:42px;width:50px;height:50px"></div>
    <div class="member-name" style="left:28px;top:100px">Marco Delane</div>
    <div class="member-name" style="left:98px;top:100px">Helena Voss</div>
    <div class="member-name" style="left:169px;top:100px">Idris Falken</div>
    <p class="member-note" style="left:30px;top:108px">Short role note for this team member goes right here.</p>
    <p class="member-note" style="left:100px;top:108px">Short role note for this team member goes right here.</p>
    <p class="member-note" style="left:171px;top:108px">Short role note for this team member goes right here.</p>
  </section>

  <section class="slide company-groups" style="left:111px;top:450px">
    <div class="tag" style="top:12px"><span>THE COMPANY</span></div>
    <div class="abs" style="left:19px;top:37px;width:104px">
      <div style="font-size:3.6px;font-weight:600">Group 1</div>
      <p class="tiny justify" style="font-size:2.4px;line-height:3.3px">A short summary of the company, its people and its goals. Replace this text with your own message to suit the topic of the slide.</p>
      <div style="font-size:3.6px;font-weight:600;margin-top:14px">Group 1</div>
      <p class="tiny justify" style="font-size:2.4px;line-height:3.3px">A short summary of the company, its people and its goals. Replace this text with your own message to suit the topic of the slide.</p>
      <div style="font-size:3.6px;font-weight:600;margin-top:14px">Group 1</div>
      <p class="tiny justify" style="font-size:2.4px;line-height:3.3px">A short summary of the company, its people and its goals. Replace this text with your own message to suit the topic of the slide.</p>
    </div>
    <div class="abs" style="left:137px;top:37px;width:104px">
      <div style="font-size:3.6px;font-weight:600">Group 1</div>
      <p class="tiny justify" style="font-size:2.4px;line-height:3.3px">A short summary of the company, its people and its goals. Replace this text with your own message to suit the topic of the slide.</p>
      <div style="font-size:3.6px;font-weight:600;margin-top:14px">Group 1</div>
      <p class="tiny justify" style="font-size:2.4px;line-height:3.3px">A short summary of the company, its people and its goals. Replace this text with your own message to suit the topic of the slide.</p>
      <div style="font-size:3.6px;font-weight:600;margin-top:14px">Group 1</div>
      <p class="tiny justify" style="font-size:2.4px;line-height:3.3px">A short summary of the company, its people and its goals. Replace this text with your own message to suit the topic of the slide.</p>
    </div>
  </section>

  <section class="slide company-text" style="left:390px;top:450px">
    <div class="tag" style="top:14px"><span>THE COMPANY</span></div>
    <div class="abs" style="left:19px;top:40px;width:220px">
      <p class="tiny justify light">Our team delivers clear strategy and steady results for every client. We plan with care, work with focus and report with honesty. This short note sets the tone for the story that follows in the next slides of the deck.</p>
      <p class="tiny justify light" style="margin-top:10px">Our team delivers clear strategy and steady results for every client. We plan with care, work with focus and report with honesty. This short note sets the tone for the story that follows in the next slides of the deck.</p>
      <p class="tiny justify light" style="margin-top:10px">Our team delivers clear strategy and steady results for every client. We plan with care, work with focus and report with honesty. This short note sets the tone for the story that follows in the next slides of the deck.</p>
      <p class="tiny justify light" style="margin-top:10px">Our team delivers clear strategy and steady results for every client. We plan with care, work with focus and report with honesty. This short note sets the tone for the story that follows in the next slides of the deck.</p>
    </div>
  </section>

  <section class="slide profile" style="left:670px;top:450px">
    <div class="portrait" role="img" aria-label="Smiling man on a phone call" style="left:20px;top:22px;width:101px;height:101px;border:0;background:radial-gradient(circle at 50% 45%,#e2d6c9,#9c8a78)"></div>
    <div class="abs" style="left:146px;top:26px">
      <div style="font-size:8.4px;font-style:italic;font-weight:600;line-height:10.5px">Brightwell<br>About Title<br>Presentation</div>
    </div>
    <p class="abs tiny justify" style="left:146px;top:64px;width:64px">A short summary of the company, its people and its goals. Replace this text with your own message to suit the topic of the slide.</p>
    <div class="social" style="left:146px;top:110px"><span></span><span></span><span></span></div>
  </section>

  <section class="slide info-pie" style="left:111px;top:607px">
    <div class="tag" style="top:17px"><span>OUR <b>INFOGRAPHIC</b></span></div>
    <svg class="abs" style="inset:0" width="257" height="145" viewBox="0 0 257 145">
      <g transform="rotate(-90 124 79)" fill="none" stroke-width="39">
        <circle cx="124" cy="79" r="19.5" stroke="#2b2b2b" stroke-dasharray="42.9 122.5" stroke-dashoffset="0"/>
        <circle cx="124" cy="79" r="19.5" stroke="#6f6f6f" stroke-dasharray="35.5 122.5" stroke-dashoffset="-42.9"/>
        <circle cx="124" cy="79" r="19.5" stroke="#bdbdbd" stroke-dasharray="15.9 122.5" stroke-dashoffset="-78.4"/>
        <circle cx="124" cy="79" r="19.5" stroke="#d6d6d6" stroke-dasharray="12.3 122.5" stroke-dashoffset="-94.3"/>
        <circle cx="124" cy="79" r="19.5" stroke="#9a9a9a" stroke-dasharray="9.8 122.5" stroke-dashoffset="-106.6"/>
        <circle cx="124" cy="79" r="19.5" stroke="#858585" stroke-dasharray="6.1 122.5" stroke-dashoffset="-116.4"/>
      </g>
      <g font-size="3.4" fill="#fff" text-anchor="middle">
        <text x="141" y="73">35%</text><text x="124" y="105">29%</text>
        <text x="105" y="92">13%</text><text x="106" y="81">10%</text>
        <text x="110" y="72">8%</text><text x="118" y="66">7%</text>
      </g>
      <g font-size="3.8" fill="#555">
        <text x="72" y="46" text-anchor="end">Unique Slides</text>
        <text x="72" y="75" text-anchor="end">Unique Slides</text>
        <text x="72" y="104" text-anchor="end">Unique Slides</text>
        <text x="176" y="46">Unique Slides</text>
        <text x="176" y="75">Unique Slides</text>
        <text x="176" y="104">Unique Slides</text>
      </g>
      <g fill="#2b2b2b"><circle cx="75" cy="45" r="1"/><circle cx="75" cy="74" r="1"/><circle cx="75" cy="103" r="1"/><circle cx="172" cy="45" r="1"/><circle cx="172" cy="74" r="1"/><circle cx="172" cy="103" r="1"/></g>
      <g font-size="2.6" fill="#bbb">
        <text x="75" y="50" text-anchor="end">Create awesome and unique</text><text x="75" y="53.5" text-anchor="end">presentation slides with these creative</text>
        <text x="75" y="79" text-anchor="end">Create awesome and unique</text><text x="75" y="82.5" text-anchor="end">presentation slides with these creative</text>
        <text x="75" y="108" text-anchor="end">Create awesome and unique</text><text x="75" y="111.5" text-anchor="end">presentation slides with these creative</text>
        <text x="176" y="50">Create awesome and unique</text><text x="176" y="53.5">presentation slides with these creative</text>
        <text x="176" y="79">Create awesome and unique</text><text x="176" y="82.5">presentation slides with these creative</text>
        <text x="176" y="108">Create awesome and unique</text><text x="176" y="111.5">presentation slides with these creative</text>
      </g>
    </svg>
  </section>

  <section class="slide info-bars" style="left:390px;top:607px">
    <div class="tag" style="top:17px"><span>OUR <b>INFOGRAPHIC</b></span></div>
    <svg class="abs" style="inset:0" width="257" height="145" viewBox="0 0 257 145">
      <g id="chartA">
        <g stroke="#eee" stroke-width=".3"><line x1="38" y1="44" x2="113" y2="44"/><line x1="38" y1="54" x2="113" y2="54"/><line x1="38" y1="64" x2="113" y2="64"/><line x1="38" y1="74" x2="113" y2="74"/><line x1="38" y1="84" x2="113" y2="84"/><line x1="38" y1="94" x2="113" y2="94"/></g>
        <g font-size="2.4" fill="#aaa" text-anchor="end"><text x="36" y="45">100</text><text x="36" y="55">80</text><text x="36" y="65">60</text><text x="36" y="75">40</text><text x="36" y="85">20</text><text x="36" y="95">0</text></g>
        <rect x="48" y="66.5" width="5.5" height="27.5" fill="#111"/>
        <rect x="54.5" y="76.5" width="5.5" height="17.5" fill="#555"/>
        <rect x="61" y="71.5" width="5.5" height="22.5" fill="#bbb"/>
        <rect x="79" y="84" width="5.5" height="10" fill="#e6e6e6"/>
        <rect x="85.5" y="76.5" width="5.5" height="17.5" fill="#bbb"/>
        <rect x="92" y="66.5" width="5.5" height="27.5" fill="#777"/>
        <rect x="98.5" y="54" width="5.5" height="40" fill="#111"/>
        <g font-size="2.6" fill="#aaa" text-anchor="middle"><text x="57" y="99">April</text><text x="92" y="99">May</text></g>
      </g>
      <use href="#chartA" x="114"/>
      <g font-size="2.5" fill="#999">
        <rect x="38" y="124" width="3" height="3" fill="#111"/><text x="43" y="126.5">Unique Infographic</text>
        <rect x="89" y="124" width="3" height="3" fill="#555"/><text x="94" y="126.5">Unique Infographic</text>
        <rect x="138" y="124" width="3" height="3" fill="#bbb"/><text x="143" y="126.5">Unique Infographic</text>
        <rect x="186" y="124" width="3" height="3" fill="#e6e6e6"/><text x="191" y="126.5">Unique Infographic</text>
      </g>
    </svg>
  </section>

  <section class="slide teams-four" style="left:670px;top:607px">
    <div class="abs center italic-title" style="left:0;right:0;top:15px;font-size:10.5px;font-weight:600">Brightwell Teams</div>
    <div class="abs" style="left:0;right:0;top:55px;bottom:0;background:var(--dark)"></div>
    <div class="portrait" role="img" aria-label="Portrait of team member" style="left:30px;top:37px;width:42px;height:42px"></div>
    <div class="portrait" role="img" aria-label="Portrait of team member" style="left:83px;top:37px;width:42px;height:42px"></div>
    <div class="portrait" role="img" aria-label="Portrait of team member" style="left:138px;top:37px;width:42px;height:42px"></div>
    <div class="portrait" role="img" aria-label="Portrait of team member" style="left:192px;top:37px;width:42px;height:42px"></div>
    <div class="member-name" style="left:21px;top:88px;font-size:4px;font-style:italic">Tessa Morrow</div>
    <div class="member-name" style="left:74px;top:88px;font-size:4px;font-style:italic">Rafael Ortin</div>
    <div class="member-name" style="left:129px;top:88px;font-size:4px;font-style:italic">Helena Voss</div>
    <div class="member-name" style="left:183px;top:88px;font-size:4px;font-style:italic">Owen Brackley</div>
    <p class="member-note" style="left:26px;top:94px;width:50px;font-size:2px;line-height:2.7px">Short role note for this team member goes right here.</p>
    <p class="member-note" style="left:79px;top:94px;width:50px;font-size:2px;line-height:2.7px">Short role note for this team member goes right here.</p>
    <p class="member-note" style="left:134px;top:94px;width:50px;font-size:2px;line-height:2.7px">Short role note for this team member goes right here.</p>
    <p class="member-note" style="left:188px;top:94px;width:50px;font-size:2px;line-height:2.7px">Short role note for this team member goes right here.</p>
    <p class="abs tiny center" style="left:28px;right:28px;top:120px;color:#ddd;font-size:2.6px;line-height:4.5px">A short summary of the company, its people and its goals. Replace this text with your own message to suit the topic of the slide.</p>
  </section>

  <section class="slide info-groups" style="left:111px;top:764px">
    <div class="tag" style="top:17px"><span>OUR <b>INFOGRAPHIC</b></span></div>
    <svg class="abs" style="inset:0" width="257" height="145" viewBox="0 0 257 145">
      <g stroke="#eee" stroke-width=".3"><line x1="38" y1="42" x2="217" y2="42"/><line x1="38" y1="53.6" x2="217" y2="53.6"/><line x1="38" y1="65.2" x2="217" y2="65.2"/><line x1="38" y1="76.8" x2="217" y2="76.8"/><line x1="38" y1="88.4" x2="217" y2="88.4"/><line x1="38" y1="100" x2="217" y2="100"/></g>
      <g font-size="2.4" fill="#aaa" text-anchor="end"><text x="36" y="43">125</text><text x="36" y="54.6">100</text><text x="36" y="66.2">75</text><text x="36" y="77.8">50</text><text x="36" y="89.4">25</text><text x="36" y="101">0</text></g>
      <rect x="46" y="92" width="7" height="8" fill="#777"/>
      <rect x="54" y="74" width="7" height="26" fill="#111"/>
      <rect x="62" y="84" width="7" height="16" fill="#bbb"/>
      <rect x="90" y="88" width="7" height="12" fill="#e6e6e6"/>
      <rect x="98" y="79" width="7" height="21" fill="#bbb"/>
      <rect x="106" y="64" width="7" height="36" fill="#111"/>
      <rect x="134" y="75" width="7" height="25" fill="#e0e0e0"/>
      <rect x="142" y="68" width="7" height="32" fill="#bbb"/>
      <rect x="150" y="86" width="7" height="14" fill="#e6e6e6"/>
      <rect x="180" y="56" width="7" height="44" fill="#111"/>
      <rect x="188" y="74" width="7" height="26" fill="#777"/>
      <rect x="196" y="88" width="7" height="12" fill="#999"/>
      <g font-size="2.6" fill="#aaa" text-anchor="middle"><text x="64" y="105">April</text><text x="102" y="105">May</text></g>
      <g font-size="2.5" fill="#999">
        <rect x="49" y="124" width="3" height="3" fill="#111"/><text x="54" y="126.5">Unique Infographic</text>
        <rect x="97" y="124" width="3" height="3" fill="#555"/><text x="102" y="126.5">Unique Infographic</text>
        <rect x="145" y="124" width="3" height="3" fill="#777"/><text x="150" y="126.5">Unique Infographic</text>
        <rect x="194" y="124" width="3" height="3" fill="#bbb"/><text x="199" y="126.5">Unique Infographic</text>
      </g>
    </svg>
  </section>

  <section class="slide closing" style="left:390px;top:764px;background:var(--dark)">
    <div class="photo" role="img" aria-label="Dark blurred photo of game pieces on a board" style="inset:0;background:radial-gradient(circle at 60% 70%,#3a3436,#262626 70%)"></div>
    <div class="abs center" style="left:0;right:0;top:30px;color:#fff;font-family:'Roboto',sans-serif">
      <div style="font-size:20px;line-height:23px">Thanks<br>For Wathing</div>
      <div style="font-size:5.8px;line-height:7.6px;margin-top:7px;font-weight:400">Harbour City, Westland<br>P : +00 4 1234 5678&nbsp; E : hello@northvale.co<br>www.northvale.co</div>
    </div>
  </section>

  <section class="slide yearly" style="left:670px;top:764px">
    <svg class="abs" style="inset:0" width="257" height="145" viewBox="0 0 257 145">
      <g stroke="#eee" stroke-width=".3"><line x1="23" y1="20" x2="240" y2="20"/><line x1="23" y1="28.5" x2="240" y2="28.5"/><line x1="23" y1="37" x2="240" y2="37"/><line x1="23" y1="45.5" x2="240" y2="45.5"/><line x1="23" y1="54" x2="240" y2="54"/><line x1="23" y1="62.5" x2="240" y2="62.5"/><line x1="23" y1="71" x2="240" y2="71"/></g>
      <g font-size="2.4" fill="#aaa" text-anchor="end"><text x="21" y="21">6</text><text x="21" y="29.5">5</text><text x="21" y="38">4</text><text x="21" y="46.5">3</text><text x="21" y="55">2</text><text x="21" y="63.5">1</text><text x="21" y="72">0</text></g>
      <rect x="32" y="34.5" width="7" height="36.5" fill="#2b2b2b"/><rect x="40" y="50.5" width="7" height="20.5" fill="#666"/><rect x="48" y="54" width="7" height="17" fill="#ccc"/><rect x="56" y="41" width="7" height="30" fill="#777"/>
      <rect x="86" y="50.5" width="7" height="20.5" fill="#2b2b2b"/><rect x="94" y="33.5" width="7" height="37.5" fill="#888"/><rect x="102" y="54" width="7" height="17" fill="#666"/><rect x="110" y="49.5" width="7" height="21.5" fill="#777"/>
      <rect x="140" y="41" width="7" height="30" fill="#2b2b2b"/><rect x="148" y="56" width="7" height="15" fill="#ccc"/><rect x="156" y="45.5" width="7" height="25.5" fill="#888"/><rect x="164" y="37" width="7" height="34" fill="#666"/>
      <rect x="194" y="32.5" width="7" height="38.5" fill="#777"/><rect x="202" y="47" width="7" height="24" fill="#666"/><rect x="210" y="28.5" width="7" height="42.5" fill="#2b2b2b"/><rect x="218" y="32.5" width="7" height="38.5" fill="#ccc"/>
      <g font-size="2.5" fill="#aaa" text-anchor="middle"><text x="48" y="75">2018</text><text x="102" y="75">2019</text><text x="156" y="75">2020</text><text x="210" y="75">2021</text></g>
      <g font-size="2.6" fill="#888">
        <rect x="34" y="80" width="2.5" height="2.5" fill="#2b2b2b"/><text x="38" y="82.5">Linkly</text>
        <rect x="62" y="80" width="2.5" height="2.5" fill="#666"/><text x="66" y="82.5">Postboard</text>
        <rect x="95" y="80" width="2.5" height="2.5" fill="#888"/><text x="99" y="82.5">Pinfold</text>
        <rect x="125" y="80" width="2.5" height="2.5" fill="#ccc"/><text x="129" y="82.5">Searchly</text>
      </g>
    </svg>
    <div class="abs" style="left:18px;top:92px;width:222px">
      <p class="tiny justify">Our team delivers clear strategy and steady results for every client. We plan with care, work with focus and report with honesty. This short note sets the tone for the story that follows in the next slides of the deck. Our team delivers clear strategy and steady results for every client. We plan with care, work with focus and report with honesty. This short note sets the tone for the story that follows in the next slides of the deck.</p>
    </div>
  </section>

  <section class="slide icons" style="left:111px;top:921px">
    <svg class="abs" role="img" aria-label="Grid of small black interface icons" style="left:24px;top:12px" width="212" height="118" viewBox="0 0 212 118">
      <defs><pattern id="iconGridA" width="15" height="14.8" patternUnits="userSpaceOnUse"><rect x="2" y="2" width="8" height="8" rx="1.5" fill="#1a1a1a"/></pattern></defs>
      <rect width="212" height="118" fill="url(#iconGridA)"/>
    </svg>
  </section>

  <section class="slide icons" style="left:390px;top:921px">
    <svg class="abs" role="img" aria-label="Grid of small black and outline business icons" style="left:24px;top:12px" width="212" height="118" viewBox="0 0 212 118">
      <defs><pattern id="iconGridB" width="15" height="14.8" patternUnits="userSpaceOnUse"><rect x="2" y="2" width="8" height="8" rx="1.5" fill="#1a1a1a"/></pattern>
      <pattern id="iconGridC" width="15" height="14.8" patternUnits="userSpaceOnUse"><rect x="2.5" y="2.5" width="7" height="7" rx="1.5" fill="none" stroke="#333" stroke-width=".8"/></pattern></defs>
      <rect width="212" height="74" fill="url(#iconGridB)"/>
      <rect y="74" width="212" height="44" fill="url(#iconGridC)"/>
    </svg>
  </section>

  <section class="slide heading-pie" style="left:670px;top:921px">
    <div class="abs" style="left:19px;top:19px">
      <div style="font-size:9.5px;font-weight:600;color:#333;line-height:10px">Heading Here</div>
      <div style="font-size:5px;color:var(--muted)">Sub Heading</div>
    </div>
    <p class="abs tiny justify" style="left:19px;top:41px;width:93px">Our team delivers clear strategy and steady results for every client. We plan with care, work with focus and report with honesty. This short note sets the tone for the story that follows in the next slides of the deck.</p>
    <p class="abs tiny justify" style="left:19px;top:102px;width:93px">A short summary of the company, its people and its goals. Replace this text with your own message to suit the topic of the slide.</p>
    <svg class="abs" style="inset:0" width="257" height="145" viewBox="0 0 257 145">
      <g transform="rotate(-90 192 76)" fill="none" stroke-width="37">
        <circle cx="192" cy="76" r="18.5" stroke="#7a7a7a" stroke-dasharray="26.7 116.2" stroke-dashoffset="0"/>
        <circle cx="192" cy="76" r="18.5" stroke="#b5b5b5" stroke-dasharray="22.1 116.2" stroke-dashoffset="-26.7"/>
        <circle cx="192" cy="76" r="18.5" stroke="#2b2b2b" stroke-dasharray="67.4 116.2" stroke-dashoffset="-48.8"/>
      </g>
      <g font-size="3.4" fill="#fff" text-anchor="middle"><text x="200" y="55">23%</text><text x="218" y="80">19%</text><text x="178" y="95">58%</text></g>
      <g font-size="3" fill="#555">
        <rect x="147" y="111" width="2.5" height="2.5" fill="#2b2b2b"/><text x="151" y="113.5">Sale</text>
        <rect x="163" y="111" width="2.5" height="2.5" fill="#7a7a7a"/><text x="167" y="113.5">Revenue</text>
        <rect x="185" y="111" width="2.5" height="2.5" fill="#555"/><text x="189" y="113.5">Profit</text>
        <rect x="201" y="111" width="2.5" height="2.5" fill="#ccc"/><text x="205" y="113.5">Expenditure</text>
      </g>
    </svg>
  </section>

</div>
</body>
</html>
```